Job application set/company logo

My resume, profile and project file need to be designed in a common, fresh business design, not too playful and colourful
Potentially a logo for my company called Quill Brook Consulting needs to be designed in a second step. My company is consulting in digitalization and business transformation.

```html
<!DOCTYPE html>
<html lang="en">
<head>
<meta charset="utf-8">
<title>Matthias Kerwald – Resume</title>
<link rel="stylesheet" href="https://fonts.googleapis.com/css2?family=Hind:wght@400;500;600;700&family=Oswald:wght@500;600&display=swap">
<style>
:root{
  --stage:#acacac;
  --paper:#ffffff;
  --navy:#2e3342;
  --panel:#e9ebea;
  --ink:#272b35;
  --rule:#7a7f8a;
}
*{margin:0;padding:0;box-sizing:border-box}
html,body{width:1200px;height:904px;overflow:hidden;background:var(--stage)}
body{font-family:"Hind",Arial,sans-serif;color:var(--ink)}
.canvas{position:relative;width:1200px;height:904px;background:var(--stage)}
.page{position:absolute;top:105px;width:491px;height:694px;background:var(--paper);border-bottom:4px solid var(--navy)}
.page--left{left:85px}
.page--right{left:624px}
.abs{position:absolute}

/* portrait */
.portrait{position:absolute;left:35px;top:21px;width:156px;height:156px;border-radius:50%;border:5px solid var(--navy);padding:3px;background:#fff}
.portrait__photo{width:100%;height:100%;border-radius:50%;background:radial-gradient(circle at 50% 40%,#c9c2bb 0%,#8d8a88 45%,#3a3d44 100%)}
.person-name{position:absolute;left:27px;top:186px;font-family:"Oswald",Arial,sans-serif;font-weight:600;font-size:23px;letter-spacing:-.4px;color:var(--navy);line-height:1;white-space:nowrap;transform:scaleX(.88);transform-origin:left top}

/* side panels */
.panel{position:absolute;background:var(--panel);border-radius:9px}
.tab{position:absolute;height:18px;background:var(--navy);color:#fff;font-weight:600;font-size:12px;line-height:19px;padding-left:14px;border-radius:0 10px 10px 0;letter-spacing:.2px}
.tab::after{content:"";position:absolute;left:0;top:18px;width:6px;height:7px;background:var(--navy);border-radius:0 0 0 6px}
.tab--main{height:20px;font-size:12.5px;line-height:21px;padding-left:8px;border-radius:0 11px 11px 0}
.tab--main::after{display:none}

.info{position:absolute;left:32px;font-size:8.8px;font-weight:500;line-height:11px;color:var(--ink)}
.info__icon{position:absolute;left:-15px;top:1px;width:9px;height:9px;border-radius:50%;background:var(--navy)}
.info__icon svg{display:block}

.section-title{position:absolute;left:27px;top:331px;font-weight:700;font-size:15px;color:var(--navy);letter-spacing:.2px}

.dotlist{position:absolute;left:29px;border-left:1px dashed #8c9099;padding-left:9px;list-style:none}
.dotlist li{position:relative;font-size:8.8px;line-height:10.9px}
.dotlist li::before{content:"";position:absolute;left:-11.5px;top:2px;width:4px;height:4px;border-radius:50%;background:var(--navy)}
.dotlist b{font-weight:600}

/* main column timeline */
.timeline{position:absolute;width:1px;background:var(--navy)}
.node{position:absolute;width:6px;height:6px;border:1.3px solid var(--navy);border-radius:50%;background:#fff}
.block{position:absolute;left:229px;width:236px}
.block h3{font-size:9.6px;font-weight:700;color:var(--navy);letter-spacing:.1px;line-height:11px}
.checks{list-style:none}
.checks li{position:relative;padding-left:10px;font-size:8.6px;line-height:11px;margin-top:4px;text-align:justify}
.checks li::before{content:"";position:absolute;left:0;top:2.5px;width:5.5px;height:5.5px;border-radius:50%;background:var(--navy)}
.checks--tight li{margin-top:3px}
.small li{font-size:7.8px;line-height:10px}
.key{font-size:8.6px;font-weight:600;padding-left:9px;margin-top:3px;line-height:9px}

.job-role{font-size:10.6px;font-weight:700;color:var(--ink);line-height:12px}
.job-head{display:flex;justify-content:space-between;align-items:flex-end;border-bottom:.8px solid var(--rule);padding-bottom:1px;line-height:11px}
.job-head strong{font-size:9.6px;font-weight:600;color:var(--ink)}
.job-head em{font-size:8px;font-weight:500}
.job-sub{font-size:9.6px;font-weight:600;line-height:11.5px}

/* right page panels */
.uni{position:absolute;left:36px;top:48px;width:150px;font-size:10.8px;line-height:12.8px;color:var(--ink)}
.uni p{margin-bottom:12px}
.ruled-dots{position:absolute;left:29px;width:1px;border-left:1px dashed #8c9099}
.mini-dot{position:absolute;width:4px;height:4px;border-radius:50%;background:var(--navy)}
.lang{position:absolute;left:36px;font-size:9.8px;line-height:11px}
.lang b{font-weight:600;display:inline-block;width:40px}
.act-label{position:absolute;left:35px;font-size:9.6px;font-weight:600;line-height:10px}
.act-rule{position:absolute;height:0;border-top:1px dotted #9ca0a8}
.icon-ph{position:absolute;width:22px;height:22px;border-radius:4px;background:linear-gradient(#cfd2d6,#b7bbc2)}
.icon-cap{position:absolute;font-size:9.8px;font-weight:500;text-align:center;width:40px;line-height:10px}
.vsep{position:absolute;width:0;border-left:1px dashed #8c9099;height:22px}
.ref{position:absolute;left:34px;width:160px;font-size:9.8px;line-height:12px}
</style>
</head>
<body>
<div class="canvas">

  <!-- ================= PAGE ONE ================= -->
  <section class="page page--left">
    <div class="portrait"><div class="portrait__photo" role="img" aria-label="Portrait photo of Matthias Kerwald in a dark suit"></div></div>
    <h1 class="person-name">MATTHIAS KERWALD</h1>

    <div class="panel" style="left:20px;top:218px;width:180px;height:104px"></div>
    <div class="tab" style="left:13px;top:222px;width:124px">PERSONAL INFOS</div>

    <div class="info" style="top:245px"><span class="info__icon"></span>17.08.1968</div>
    <div class="info" style="top:261px"><span class="info__icon"><svg width="9" height="9" viewBox="0 0 9 9"><circle cx="4.5" cy="3.8" r="1.6" fill="none" stroke="#fff" stroke-width=".9"/></svg></span>Weidenstraße 14<br>53119 Bonn, Germany</div>
    <div class="info" style="top:286px"><span class="info__icon"><svg width="9" height="9" viewBox="0 0 9 9"><rect x="2" y="2.8" width="5" height="3.4" fill="none" stroke="#fff" stroke-width=".8"/><path d="M2 3l2.5 1.8L7 3" fill="none" stroke="#fff" stroke-width=".7"/></svg></span>Matthias.Kerwald@postmail.de</div>
    <div class="info" style="top:302px"><span class="info__icon"></span>www.proflink.net/in/matthiaskerwald</div>

    <h2 class="section-title">QUALIFICATIONS</h2>

    <div class="panel" style="left:20px;top:349px;width:180px;height:158px"></div>
    <div class="tab" style="left:13px;top:353px;width:140px">CORE COMPETENCIES</div>
    <ul class="dotlist" style="top:374px;width:162px">
      <li><b>Passionate Digital Transformation Leader</b> with track record of launching and growing business</li>
      <li style="margin-top:5px"><b>Entrepreneurial background</b> with network to global innovation hubs</li>
      <li style="margin-top:5px"><b>Strong Product &amp; Innovation competence</b> with a clear understanding of market needs</li>
      <li style="margin-top:5px"><b>Track record in driving partnerships</b> into highly successful collaborations</li>
    </ul>

    <div class="panel" style="left:20px;top:517px;width:180px;height:163px"></div>
    <div class="tab" style="left:13px;top:521px;width:140px">ACCOMPLISHMENTS</div>
    <ul class="dotlist" style="top:542px;width:160px">
      <li>Mentor at Corelan's Spark program for start-ups</li>
      <li style="margin-top:5px">Crash Course in Data Science at The Harlowvale University</li>
      <li style="margin-top:5px">Intro to Blockchain Technology at Lindhaven Institute</li>
      <li style="margin-top:5px">PSM 1, Certified Scrum Master, Agile Guild</li>
      <li style="margin-top:5px">Leadership Excellence Program at Valcrest Business School</li>
    </ul>

    <!-- profile column -->
    <div class="tab tab--main" style="left:218px;top:26px;width:176px">PROFILE &amp; ACHIEVEMENTS</div>
    <div class="timeline" style="left:221px;top:53px;height:409px"></div>
    <span class="node" style="left:218px;top:52px"></span>
    <span class="node" style="left:218px;top:137px"></span>
    <span class="node" style="left:218px;top:264px"></span>

    <div class="block" style="top:51px">
      <h3>GUIDING ENTREPRENERIAL INNOVATIONS</h3>
      <ul class="checks checks--tight">
        <li style="margin-top:1px">Define a way forward for Velorix's Messaging business</li>
        <li>Shape a venture for Norvion in the eMobility segment</li>
        <li>Build a joint venture of Nordwell Telekom and Optara for the development of connected smart glasses</li>
      </ul>
    </div>
    <div class="block" style="top:136px">
      <h3>LEADING GLOBAL PARTNERSHIP NETWORKS</h3>
      <ul class="checks checks--tight">
        <li style="margin-top:1px">Overcome strategic objectives and form an alliance of Searchly and Velorix in Messaging</li>
        <li>Position Nordwell Telekom as first choice for Pomeline smartphones with a purchase volume of more than 2 billion euro</li>
        <li>Create exclusive advantages for Nordwell Telekom customers through partnerships with major innovators like Pomeline and Riverstore</li>
      </ul>
    </div>
    <div class="block" style="top:263px">
      <h3>DELIVERY-ORIENTED PRODUCT LEADER</h3>
      <ul class="checks checks--tight">
        <li style="margin-top:1px">Manage the roll out of new GSM-R Units to &gt;5000 vehicles for Railnet AG in logistics and technical integration</li>
        <li>Open the door for IoT business of Quentra to access European telcos</li>
        <li>Develop a consistent Violet@home experience and build the corresponding device portfolio supporting DSL, TV, Smart Home</li>
      </ul>
    </div>

    <!-- experience -->
    <div class="tab tab--main" style="left:218px;top:388px;width:178px">EXPERIENCE (EXEMPLARY)</div>
    <div class="timeline" style="left:221px;top:418px;height:272px"></div>
    <span class="node" style="left:218px;top:416px"></span>

    <div class="block" style="top:412px">
      <div class="job-role">SENIOR ADVISOR (self-employed)</div>
      <div class="job-head" style="margin-top:2px"><strong>Incubra Corporate Startups</strong><em>10/2020 – Present</em></div>
      <ul class="checks checks--tight">
        <li>Venture building (e.g. with Norvion and NT)</li>
        <li>Derive a product strategy and go to market plan</li>
      </ul>
      <div class="key">Key Success:</div>
      <ul class="checks"><li style="margin-top:2px">Successful start of Velora, the Norvion eMobility venture</li></ul>
    </div>

    <div class="block" style="top:507px">
      <div class="job-head"><strong>Quentra Systems</strong><em>08/2021 – Present</em></div>
      <ul class="checks checks--tight">
        <li>Define a strategy how to approach telco carriers</li>
        <li>Evaluate business models to engage with distributors</li>
      </ul>
      <div class="key" style="margin-top:5px">Key Success:</div>
      <ul class="checks"><li style="margin-top:2px">Growth through new distribution channels via carriers</li></ul>
    </div>

    <div class="block" style="top:591px">
      <div class="job-head"><strong>Velorix</strong><em>04/2021 – 04/2022</em></div>
      <ul class="checks checks--tight">
        <li>Evaluation of the global messaging business</li>
        <li>Define a new strategy for messaging in Velorix</li>
        <li>Implement a new independent business unit for SaaS</li>
      </ul>
      <div class="key">Key Success:</div>
      <ul class="checks"><li style="margin-top:2px">Successful start of the new business unit</li></ul>
    </div>
  </section>

  <!-- ================= PAGE TWO ================= -->
  <section class="page page--right">
    <!-- university -->
    <div class="panel" style="left:20px;top:21px;width:180px;height:156px"></div>
    <div class="tab" style="left:14px;top:26px;width:98px">UNIVERSITY</div>
    <div class="ruled-dots" style="top:52px;height:110px"></div>
    <span class="mini-dot" style="left:27.5px;top:51px"></span>
    <span class="mini-dot" style="left:27.5px;top:99px"></span>
    <div class="uni">
      <p>Executive Leadership Development Program at Kestrow Graduate School of Business (2016)</p>
      <p>Diploma in Electrical Engineering at Technische Hochschule Rheinberg (THR) (1987-1994)</p>
    </div>

    <!-- languages -->
    <div class="panel" style="left:20px;top:194px;width:180px;height:71px"></div>
    <div class="tab" style="left:14px;top:198px;width:98px">LANGUAGES</div>
    <div class="ruled-dots" style="top:222px;height:32px"></div>
    <span class="mini-dot" style="left:27.5px;top:226px"></span>
    <span class="mini-dot" style="left:27.5px;top:246px"></span>
    <div class="lang" style="top:222px"><b>German</b>Native</div>
    <div class="lang" style="top:242px"><b>English</b>Full professional proficiency</div>

    <!-- activities -->
    <div class="panel" style="left:20px;top:282px;width:180px;height:214px"></div>
    <div class="tab" style="left:14px;top:286px;width:98px">ACTIVITIES</div>
    <div class="ruled-dots" style="top:313px;height:172px"></div>
    <span class="node" style="left:26.5px;top:313px;width:5px;height:5px"></span>
    <span class="node" style="left:26.5px;top:378px;width:5px;height:5px"></span>
    <span class="node" style="left:26.5px;top:433px;width:5px;height:5px"></span>

    <div class="act-label" style="top:312px">SPORT:</div>
    <div class="act-rule" style="left:70px;top:320px;width:120px"></div>
    <div class="icon-ph" style="left:45px;top:326px" role="img" aria-label="Skiing icon"></div>
    <div class="icon-ph" style="left:84px;top:326px" role="img" aria-label="Tennis icon"></div>
    <div class="icon-ph" style="left:123px;top:326px" role="img" aria-label="Hiking icon"></div>
    <div class="icon-ph" style="left:163px;top:326px" role="img" aria-label="Yoga icon"></div>
    <div class="vsep" style="left:75px;top:330px"></div>
    <div class="vsep" style="left:114px;top:330px"></div>
    <div class="vsep" style="left:153px;top:330px"></div>
    <div class="icon-cap" style="left:36px;top:352px">Skiing</div>
    <div class="icon-cap" style="left:75px;top:352px">Tennis</div>
    <div class="icon-cap" style="left:114px;top:352px">Hiking</div>
    <div class="icon-cap" style="left:154px;top:352px">Yoga</div>

    <div class="act-label" style="top:377px">MUSIC:</div>
    <div class="act-rule" style="left:68px;top:385px;width:122px"></div>
    <div class="icon-ph" style="left:34px;top:393px;width:28px;height:25px" role="img" aria-label="Grand piano icon"></div>
    <div class="abs" style="left:71px;top:401px;font-size:9.8px;font-weight:500">Classical Piano</div>

    <div class="act-label" style="top:432px;left:33px">TRAVELLING:</div>
    <div class="act-rule" style="left:92px;top:440px;width:98px"></div>
    <div class="icon-ph" style="left:46px;top:447px" role="img" aria-label="Map of Europe"></div>
    <div class="icon-ph" style="left:99px;top:447px" role="img" aria-label="Map of Africa"></div>
    <div class="icon-ph" style="left:152px;top:447px" role="img" aria-label="Map of America"></div>
    <div class="vsep" style="left:85px;top:450px"></div>
    <div class="vsep" style="left:138px;top:450px"></div>
    <div class="icon-cap" style="left:38px;top:472px">Europe</div>
    <div class="icon-cap" style="left:90px;top:472px">Africa</div>
    <div class="icon-cap" style="left:143px;top:472px">America</div>

    <!-- references -->
    <div class="panel" style="left:20px;top:514px;width:180px;height:158px"></div>
    <div class="tab" style="left:14px;top:518px;width:98px">REFERENCES</div>
    <div class="ruled-dots" style="top:542px;height:112px"></div>
    <span class="mini-dot" style="left:27.5px;top:544px"></span>
    <span class="mini-dot" style="left:27.5px;top:580px"></span>
    <span class="mini-dot" style="left:27.5px;top:627px"></span>
    <div class="ref" style="top:541px">Reinhard Albrecht, CEO Nordwell Telekom</div>
    <div class="ref" style="top:577px">Stefan Moorbach, SVP Global Strategic Projects and Marketing Partnerships, Nordwell Telekom</div>
    <div class="ref" style="top:624px">Luc Verand, formerly CEO Taikon Corporation</div>

    <!-- career continued -->
    <div class="timeline" style="left:221px;top:26px;height:644px"></div>
    <span class="node" style="left:218px;top:106px"></span>
    <span class="node" style="left:218px;top:456px"></span>

    <div class="block" style="top:22px">
      <div class="job-head"><strong>kx7Consulting</strong><em>10/2020 – 12/2022</em></div>
      <ul class="checks checks--tight"><li style="margin-top:2px">Steering of a group wide exchange of GSM-R equipment</li></ul>
      <div class="key" style="margin-top:5px">Key Success:</div>
      <ul class="checks"><li style="margin-top:0">Improvement of the mobile connectivity experience for customers of the Railnet AG</li></ul>
    </div>

    <div class="block" style="top:103px">
      <div class="job-role">NORDWELL TELEKOM AG, BONN</div>
      <div class="job-sub" style="margin-top:4px">Senior Vice</div>
      <div class="job-head"><strong>President Connected Devices</strong><em>08/2011 – 07/2020</em></div>
      <ul class="checks checks--tight">
        <li>Management of the global partnerships with Pomeline, Searchly, Hanseong</li>
        <li>Board member of Lentio Inc, a JV of NT and Optara AG</li>
        <li>Driving the entire portfolio of devices for the NT group including Wearables, Voice Controlled Devices and Virtual Reality Glasses</li>
      </ul>
      <div class="key" style="margin-top:4px">Key Success:</div>
      <ul class="checks small checks--tight">
        <li style="margin-top:1px">Managing a turnover of more than 3 billion euros with devices across the Nordwell Telekom group</li>
        <li>Development of the first Violet Voice Speaker</li>
        <li>Foundation of the Lentio joint venture</li>
      </ul>
    </div>

    <div class="block" style="top:305px">
      <div class="job-sub">Vice President</div>
      <div class="job-head"><strong>Product Management Mobile</strong><em>04/2008 – 07/2011</em></div>
      <ul class="checks checks--tight">
        <li>Introduction of the international portfolio of mobile phones in Nordwell Telekom</li>
        <li>Project lead for key initiatives, e.g. introduction of Orbit OS</li>
      </ul>
      <div class="key" style="margin-top:5px">Key Success:</div>
      <ul class="checks checks--tight">
        <li style="margin-top:1px">Successful introduction of the first Orbit OS phone in an exclusive partnership with Searchly and Taikon</li>
        <li>Development of the NT App portfolio for Pomeline OS and Orbit OS</li>
      </ul>
    </div>

    <div class="block" style="top:453px">
      <div class="job-head" style="border-bottom:none"><strong style="font-size:9.8px;font-weight:700">NORDWELL MOBILE INT., BONN</strong><em>09/1994 – 03/2008</em></div>
      <div class="job-sub" style="font-size:8.8px;line-height:10px;border-top:.8px solid var(--rule);padding-top:1px">Head of Client Integration/ISP Products</div>
      <ul class="checks checks--tight">
        <li style="margin-top:0">Conception and development of a NM-branded mobile phone</li>
        <li>Transformation of product management from voice-centric into mobile internet business</li>
      </ul>
    </div>

    <div class="block" style="top:546px">
      <div class="job-sub" style="font-size:8.8px;line-height:10px">Project Lead Personal Communication Services</div>
      <ul class="checks"><li style="margin-top:0">Project lead of the first FMC product combining fixed and mobile communication on one bill with one device and one service</li></ul>
    </div>

    <div class="block" style="top:608px">
      <div class="job-sub" style="font-size:8.8px;line-height:10px">Project Engineering</div>
      <ul class="checks checks--tight">
        <li style="margin-top:0">Project lead “Short Message Service Center”</li>
        <li>Voice quality assurance: Design of a new measurement system and implementation in C++</li>
        <li>Audits of system technology suppliers</li>
      </ul>
    </div>
  </section>

</div>
</body>
</html>
```